Our Server Lantern requires an Email Marketing Design template

Our Server Lantern are a rapidly expanding UK based internet hosting company that have just re-branded through Pixel Meadow.
We provide internet based services such as website hosting, dedicated and managed servers, domain names as well as email solutions to name a few. We pride ourselves on being able to provide a comprehensive, secure, future proofed and scalable platform for our clients to communicate and do business on.
Our Server Lantern are looking to go live with a new website on 1st August. In preparation for this we would like to have an HTML Email Template designed for our launch!
We are also having a really big push on the reseller market allowing potential resellers and their end users to manage their own services via a consolidated portal with many features and functions that will grow over time.

Target Market(s)
We have 3 core target markets, the end user who would be the likes of web designers or developers. A reseller market who would want to resell our hosted services and the final target market would be a business client that would want high end server and hosting solutions.
Industry/Entity Type
Internet Service Provider
Requirements
Must have
- To ensure it is inline with the new brand (see attached files).

```html
<!DOCTYPE html>
<html lang="en">
<head>
<meta charset="utf-8">
<title>Our Server Lantern – Launch Email</title>
<link rel="stylesheet" href="https://fonts.googleapis.com/css2?family=Jost:wght@400;500;600;700&display=swap">
<style>
:root{
  --page:#eeeeee;
  --ink:#2b2b2b;
  --muted:#777777;
  --grey-band:#cfcfcf;
  --charcoal:#3a3a3a;
  --mint:#7dc79c;
  --mint-soft:#d3f2e1;
  --mint-deep:#5dbd8a;
  --teal:#1bb5b3;
  --teal-deep:#176563;
  --teal-ink:#0f5352;
  --yellow:#f5d949;
  --olive:#6d5c16;
  --navy:#1f4d79;
  --night:#252a33;
  --white:#ffffff;
  --brand:#2fae9b;
}
*{box-sizing:border-box;margin:0;padding:0}
html,body{width:1200px;height:4000px;overflow:hidden}
body{background:var(--page);font-family:"Jost",sans-serif;color:var(--ink);position:relative}
.email{position:absolute;left:120px;top:0;width:960px;overflow:hidden}

/* header / hero */
.hero{position:relative;height:577px;background:linear-gradient(180deg,#f7f7f7,#ececec);overflow:hidden}
.hero-photo{position:absolute;left:608px;top:170px;width:352px;height:407px;background:linear-gradient(160deg,#f4f1ec,#d9cfc3 60%,#c7bba9)}
.brand{position:absolute;left:50px;top:68px;display:flex;align-items:center;gap:18px}
.brand-dot{width:62px;height:62px;border-radius:50%;background:var(--brand)}
.brand-name{font-size:30px;font-weight:500;color:var(--teal-ink);line-height:1}
.nav{position:absolute;right:6px;top:82px;display:flex;gap:50px}
.nav a{font-size:23px;font-weight:600;color:#a9a9a9;text-decoration:none;letter-spacing:.5px}
.hero-title{position:absolute;left:50px;top:250px;font-size:70px;font-weight:700;line-height:.95;color:#2e2e2e;letter-spacing:-1px;z-index:1}
.hero-sub{position:absolute;left:50px;top:395px;width:440px;font-size:24px;line-height:1.2;color:var(--muted);z-index:1}

.band-grey{height:93px;background:var(--grey-band);display:flex;align-items:center;padding-left:50px;font-size:44px;font-weight:700;color:#2e2e2e}
.intro{height:350px;background:var(--charcoal);color:var(--white);padding:85px 55px 0}
.intro h2{font-size:52px;font-weight:700;margin-bottom:22px;letter-spacing:-.5px}
.intro p{font-size:25px;line-height:1.38;width:850px}
.band-mint{height:80px;background:var(--mint);display:flex;align-items:center;padding-left:55px;font-size:31px;font-weight:700;color:var(--white)}

/* plans */
.plan{position:relative;display:flex}
.plan-copy{padding:100px 48px 0;flex-shrink:0}
.plan-copy h3{font-size:33px;font-weight:600;line-height:1.15;margin-bottom:24px}
.plan-copy .desc{font-size:17px;line-height:1.45;margin-bottom:55px}
.plan-copy .from{font-size:18px}
.plan-copy .price{font-size:48px;font-weight:700;line-height:1.1;margin-bottom:30px;white-space:nowrap}
.plan-copy .price span{font-size:18px;font-weight:400}
.btn{display:inline-block;font-size:21px;font-weight:600;padding:14px 30px;color:var(--white);text-decoration:none;white-space:nowrap}
.photo{height:100%;flex-shrink:0}

.plan-shared{height:615px}
.plan-shared .plan-copy{width:314px;background:var(--mint-soft);color:#2e2e2e}
.plan-shared .desc{color:#8a9a92}
.plan-shared .price{color:var(--mint-deep)}
.plan-shared .btn{background:var(--mint-deep)}
.plan-shared .photo{width:646px;background:linear-gradient(135deg,#e8ece9,#b9c7b4 45%,#6f8c55)}

.plan-dedicated{height:605px}
.plan-dedicated .photo{width:646px;background:linear-gradient(135deg,#6f4a35,#2f5660 55%,#2c8d93)}
.plan-dedicated .plan-copy{width:314px;background:var(--teal);color:var(--teal-ink);padding-left:44px;padding-right:20px}
.plan-dedicated .desc{color:var(--white)}
.plan-dedicated .from{color:var(--white)}
.plan-dedicated .price span{color:var(--white)}
.plan-dedicated .btn{background:var(--teal-deep)}

.plan-value{height:610px}
.plan-value .plan-copy{width:360px;background:var(--yellow);color:#222;padding-left:55px}
.plan-value .desc{color:#4a4320}
.plan-value .btn{background:var(--olive)}
.plan-value .photo{width:600px;background:linear-gradient(135deg,#d8d8d5,#8a8f93 50%,#3b3d45)}

.promo{height:120px;background:var(--navy);color:var(--white);text-align:center;padding-top:14px}
.promo h2{font-size:46px;font-weight:700;line-height:1.1}
.promo p{font-size:20px}

.trust{height:350px;display:flex}
.trust-copy{width:480px;background:var(--night);color:var(--white);padding:62px 50px 0}
.trust-copy h2{font-size:56px;font-weight:700;line-height:.95;margin-bottom:26px}
.trust-copy p{font-size:25px;line-height:1.3}
.trust .photo{width:480px;background:linear-gradient(135deg,#eef0f2,#c9b2a0 55%,#9a5e3f)}

.features{height:315px;background:var(--white);display:flex;padding:45px 40px 0}
.feature{flex:1;text-align:center;padding:0 14px}
.feature svg{width:62px;height:62px;margin-bottom:10px}
.feature h4{font-size:27px;font-weight:600;line-height:1.1;margin-bottom:14px}
.feature p{font-size:16px;line-height:1.35;color:#555}

.legal{position:absolute;left:120px;top:3728px;width:960px;font-size:17px;line-height:1.45;color:#333}
.legal a{color:var(--navy);font-weight:600}
.social{position:absolute;left:505px;top:3920px;display:flex;gap:48px}
.social span{width:24px;height:24px;border-radius:50%;background:#8a8a8a;display:block}
</style>
</head>
<body>
<main class="email">
  <header class="hero">
    <div class="hero-photo" role="img" aria-label="Smiling woman with glasses at a desk with a laptop in a bright office"></div>
    <div class="brand"><span class="brand-dot"></span><span class="brand-name">Our Server Lantern</span></div>
    <nav class="nav"><a href="#">ABOUT</a><a href="#">CONTACT</a><a href="#">SUPPORT</a></nav>
    <h1 class="hero-title">WEB HOSTING<br>MADE EASY.</h1>
    <p class="hero-sub">Hassle-free web hosting to start your online adventure now.</p>
  </header>

  <div class="band-grey">FAST, SECURE AND RELIABLE.</div>

  <section class="intro">
    <h2>PAY LESS. GET MORE.</h2>
    <p>Build your fast, secure and reliable Hosting Lantern. Whether you are trying to start an online business, share your stories on a blog or sell products.. your Lantern understands all your hosting needs.</p>
  </section>

  <div class="band-mint">CHOOSE YOUR PERFECT HOSTING PLAN.</div>

  <section class="plan plan-shared">
    <div class="plan-copy">
      <h3>Shared Web Hosting</h3>
      <p class="desc">Suitable for individuals and small businesses.</p>
      <p class="from">Starting at</p>
      <p class="price">£3.99<span>/month</span></p>
      <a class="btn" href="#">KNOW MORE</a>
    </div>
    <div class="photo" role="img" aria-label="Group of young friends gathered around a computer screen"></div>
  </section>

  <section class="plan plan-dedicated">
    <div class="photo" role="img" aria-label="Man relaxing with hands behind his head in front of a brick wall"></div>
    <div class="plan-copy">
      <h3>Dedicated Servers</h3>
      <p class="desc">Your best choice for high-traffic and resource-intensive sites for complete control.</p>
      <p class="from">Starting at</p>
      <p class="price">£127.99<span>/month</span></p>
      <a class="btn" href="#">KNOW MORE</a>
    </div>
  </section>

  <section class="plan plan-value">
    <div class="plan-copy">
      <h3>Dedicated Servers</h3>
      <p class="desc">Your best choice for high-traffic and resource-intensive sites for complete control.</p>
      <p class="from">Starting at</p>
      <p class="price">£16.97<span>/month</span></p>
      <a class="btn" href="#">KNOW MORE</a>
    </div>
    <div class="photo" role="img" aria-label="Businessman working on a laptop beside stacked office folders"></div>
  </section>

  <section class="promo">
    <h2>ENJOY 30% OFF NEW PURCHASES.</h2>
    <p>Use promo code d1R03D in your cart when you order. Expires June 30, 2015.</p>
  </section>

  <section class="trust">
    <div class="trust-copy">
      <h2>WHY<br>TRUST US?</h2>
      <p>Our Server Lantern is effective cost, easy for novices,suitable for experts, and has..</p>
    </div>
    <div class="photo" role="img" aria-label="Smiling woman leaning beside a laptop"></div>
  </section>

  <section class="features">
    <div class="feature">
      <svg viewBox="0 0 62 62"><rect x="12" y="6" width="38" height="50" rx="3" fill="#5dbd8a"/><rect x="18" y="16" width="26" height="4" fill="#fff"/><rect x="18" y="26" width="26" height="4" fill="#fff"/><rect x="18" y="36" width="18" height="4" fill="#fff"/></svg>
      <h4>Best value domain names</h4>
      <p>Instant domain registration of over 50 types of domains from around the world.</p>
    </div>
    <div class="feature">
      <svg viewBox="0 0 62 62"><circle cx="31" cy="31" r="24" fill="none" stroke="#e2463c" stroke-width="12" stroke-dasharray="19 18.7"/><circle cx="31" cy="31" r="24" fill="none" stroke="#e2463c" stroke-width="2"/></svg>
      <h4>24/7<br>Free support</h4>
      <p>If you have questions, our team have the answers to help when you need it. Anytime.</p>
    </div>
    <div class="feature">
      <svg viewBox="0 0 62 62"><circle cx="31" cy="31" r="20" fill="none" stroke="#8a8f96" stroke-width="6" stroke-dasharray="6 4.5"/><circle cx="31" cy="31" r="15" fill="#8a8f96"/><circle cx="31" cy="31" r="6" fill="#fff"/></svg>
      <h4>Free<br>migration</h4>
      <p>Free of charge service to migrate one or all your servers to our hosting platform.</p>
    </div>
    <div class="feature">
      <svg viewBox="0 0 62 62"><rect x="6" y="14" width="50" height="34" rx="4" fill="#3a7fc4"/><rect x="6" y="21" width="50" height="6" fill="#1f4d79"/><rect x="12" y="36" width="16" height="4" fill="#fff"/></svg>
      <h4>No hidden charges</h4>
      <p>Fully inclusive with everything clearly stated in our plans with no hidden extras.</p>
    </div>
  </section>
</main>

<footer class="legal">
  <p>Please do not reply to this email. Emails sent to this address will not be answered.</p>
  <p><a href="#">Click here</a> to unsubscribe or manage your email preferences.</p>
  <p>Copyright © 2015 OUR SERVER LANTERN, LLC. 412 HARBOUR LANE, PIXEL MEADOW, 87000.</p>
  <p>All rights reserved.</p>
</footer>
<div class="social" aria-label="Social links"><span></span><span></span><span></span></div>
</body>
</html>
```